Two Versions of a Business Card for a Lawyer

Summary: I need a logo and a business card. The business card is two-sided and comes in two versions. One version is conservative, the other is slightly different with one or more pink embellishments in the logo or somewhere else in the business card.
I'm about to start off as a sole practitioner in criminal and immigration law. I'll largely be working with marginalised communities and in areas of social justice. One of my main focuses will be gendered violence, I'm hoping to specialise my practice towards representing victims of domestic and sexual violence and sex workers. I want a business card which would attract this clientele and make them feel safe to speak with me. I'd also like it to communicate a sense of hope.
However, the business card still has to be very conservative as the legal profession is very stuffy. So I was thinking of having two versions of the same card, one would be very straight forward while the other would have a **pink embellishment** or perhaps several. For example, if the scales of justice were used in the design, maybe the second version would have a pink flower about to bloom on the scale somewhere. Or maybe it's my logo that is different and pink.
While both designs have to be pretty conservative, I still want it to give off a sense that I'm alternative and think outside the box. With lawyers, I think a little bit of deviation goes a long way (less is more).
As far as colour goes (other than the pink embellishment), I was thinking something monochromatic, probably black and white but I am open to considering more colours. I personally love colour, and would love to use more colour, but am hesitant because of the nature of the profession. If you can find a way to use more colour while keeping it conservative and letting the pink pop, I'd be pretty pleased.
In general, I would prefer a clean simplistic design and logo. It should be immediately obvious that I'm a lawyer just by glancing at the card. I'm open to symbols of law, like the scales of justice or lady justice or something else. However, I don't want it to be the same as everyone else's.
Eventually, the design/style should be easy to recreate in the form of a website.
As far as the logo goes, it would probably use a circle as my last name starts with the letter "O". It can be very simple, with just my name and "Barrister & Solicitor". I don't currently have a logo, but the winning designer will be invited to provide a separate file for just the logo for an additional fee (I think it was CA$99). (Please ignore the uploaded logo file, it just wouldn't let me continue without uploading something).
As for the information that should go into the card, I'm still finalizing my address and phone number. So please use a placeholder for now.
Target Market(s)
Women, victims of sexual or domestic violence, refugees, people in need of legal services
Industry/Entity Type
Lawyer
Contact Information for Business Card
Maren Vickery
Barrister & Solicitor
LL.B., B.C.L., B.F.A.
Criminal & Immigration Law
Street address
Toronto, ON
Postal Code
Phone number
Fax number
Email
Logo Text
Maren Vickery, Barrister & Solicitor
Requirements
Must have
- Two versions
- One with pink
- Simplistic
Nice to have
- Maybe more colour
Should not have
- Not too conservative
- Not too predictable

```html
<!DOCTYPE html>
<html lang="en">
<head>
<meta charset="utf-8">
<title>Maren Vickery – Business Card</title>
<link href="https://fonts.googleapis.com/css2?family=Crimson+Text:ital,wght@1,400;1,600;1,700&display=swap" rel="stylesheet">
<style>
  :root {
    --card-bg: #ffffff;
    --pink: #d585c4;
    --pink-soft: #ecc3e2;
    --pink-faint: #f8e9f4;
  }
  * { margin: 0; padding: 0; box-sizing: border-box; }
  html, body {
    width: 686px;
    height: 1200px;
    overflow: hidden;
    background: var(--card-bg);
  }
  .card {
    position: relative;
    width: 686px;
    height: 1200px;
    background: var(--card-bg);
    font-family: "Crimson Text", "Times New Roman", serif;
    font-style: italic;
    color: var(--pink);
  }
  .flourish-top {
    position: absolute;
    left: 46px;
    top: 0;
    width: 594px;
    height: 170px;
    background: radial-gradient(ellipse at 50% 40%, var(--pink-soft) 0%, var(--pink-faint) 55%, rgba(255,255,255,0) 75%);
  }
  .frame-arch {
    position: absolute;
    left: 0;
    top: 0;
  }
  .name {
    position: absolute;
    left: 22px;
    top: 259px;
    font-size: 72px;
    line-height: 72px;
    font-weight: 400;
  }
  .title {
    position: absolute;
    left: 23px;
    font-size: 34px;
    line-height: 34px;
    font-weight: 700;
  }
  .title--role { top: 349px; }
  .title--degrees { top: 390px; }
  .practice {
    position: absolute;
    left: 23px;
    top: 473px;
    font-size: 40px;
    line-height: 40px;
    font-weight: 600;
  }
  .contact {
    position: absolute;
    left: 23px;
    top: 596px;
    list-style: none;
    font-size: 28px;
    line-height: 28px;
    font-weight: 700;
  }
  .contact li { height: 56.6px; }
  .rule {
    position: absolute;
    left: 9px;
    width: 668px;
    height: 2px;
    background: var(--pink);
  }
  .rule--upper { top: 991px; }
  .rule--lower { top: 1081px; }
  .flourish-bottom {
    position: absolute;
    left: 183px;
    top: 1000px;
    width: 320px;
    height: 70px;
    background: radial-gradient(ellipse at 50% 50%, var(--pink-soft) 0%, var(--pink-faint) 55%, rgba(255,255,255,0) 75%);
  }
</style>
</head>
<body>
  <div class="card">
    <svg class="frame-arch" width="686" height="240" viewBox="0 0 686 240" aria-hidden="true">
      <path d="M6 220 C 6 120, 120 80, 343 78 C 566 80, 680 120, 680 220" fill="none" stroke="var(--pink)" stroke-width="2"/>
    </svg>
    <div class="flourish-top" role="img" aria-label="Decorative pink scroll flourish crowning the card"></div>

    <h1 class="name">Maren Vickery</h1>
    <p class="title title--role">Barrister &amp; Solicitor</p>
    <p class="title title--degrees">LL.B., B.C.L., B.F.A.</p>
    <p class="practice">Criminal &amp; Immigration Law</p>

    <ul class="contact">
      <li>Street address</li>
      <li>Toronto, ON</li>
      <li>Postal Code</li>
      <li>Phone number</li>
      <li>Fax number</li>
      <li>Email</li>
    </ul>

    <div class="rule rule--upper"></div>
    <div class="flourish-bottom" role="img" aria-label="Decorative pink scroll flourish between the footer rules"></div>
    <div class="rule rule--lower"></div>
  </div>
</body>
</html>
```